Small beauty therapy room here in melbourne needs a simple but classy business card

I am after business cards for a small beauty therapy room operating from a hair salon in a rich area of melbourne. My main job is waxing, facials and tinting.

Target Market(s)

all ages

Industry/Entity Type

Beauty Salon

Contact Information for Business Card

The name of the business is Marisol's Beauty Room id like this on the front with a pattern of some kind but still simple.
I am after a business card that is either white and silver/icy green, or a dark charcoal grey with icy green colour and pattern, or even black and white, I'm quite flexible.

On the back id like it to have
Marisol Quenteli
Beauty Therapist

contact number: 0412 963 174
email: marisolquenteli@examplemail.net
website: www.marisolsbeautyroom.example.au

address:3/218-226 Ferrow Rd, Kelsby VIC 3187
with the Chatterbook and snapfolio logos only
I'm very flexible and open so anything creative and simple would be great :)

Font styles to use
Serif
Sans Serif
Decorative

Colors
cfeae6
ffffff
c6c6c6

Requirements
Must have
• classy, elegance, simple

```html
<!DOCTYPE html>
<html lang="en">
<head>
<meta charset="utf-8">
<title>Marisol's Beauty Room – Business Card</title>
<link rel="stylesheet" href="https://fonts.googleapis.com/css2?family=Abril+Fatface&family=Jost:wght@400;500&display=swap">
<style>
  :root {
    --ink: #000000;
    --icy-mint: #cfeae6;
    --white: #ffffff;
    --divider: #5a5a5a;
  }
  html, body {
    margin: 0;
    padding: 0;
    width: 1000px;
    height: 1200px;
    overflow: hidden;
    background: var(--ink);
  }
  .canvas {
    position: relative;
    width: 1000px;
    height: 1200px;
    background: var(--ink);
    overflow: hidden;
  }
  .card-front, .card-back {
    position: absolute;
    left: 0;
    width: 1000px;
  }
  .card-front { top: 0; height: 594px; }
  .card-back { top: 595px; height: 605px; border-top: 1px solid var(--divider); }

  /* Front: brand */
  .brand-ornament {
    position: absolute;
    left: 138px;
    top: 258px;
    width: 118px;
    height: 94px;
    border-radius: 8px;
    background: var(--white);
  }
  .brand-rule {
    position: absolute;
    left: 261px;
    top: 240px;
    width: 3px;
    height: 126px;
    background: var(--white);
  }
  .brand-name {
    margin: 0;
    font-weight: 400;
  }
  .brand-name__main {
    position: absolute;
    left: 290px;
    top: 203px;
    font-family: "Abril Fatface", serif;
    font-size: 118px;
    line-height: 1;
    color: var(--icy-mint);
  }
  .brand-name__sub {
    position: absolute;
    left: 293px;
    top: 334px;
    font-family: "Jost", sans-serif;
    font-weight: 500;
    font-size: 29px;
    line-height: 1;
    letter-spacing: 0.27em;
    text-transform: uppercase;
    color: var(--white);
  }

  /* Back: person */
  .person {
    position: absolute;
    right: 613px;
    top: 234px;
    text-align: right;
    color: var(--white);
  }
  .person__first {
    display: block;
    font-family: "Abril Fatface", serif;
    font-size: 62px;
    line-height: 1;
  }
  .person__last {
    display: block;
    margin-top: 6px;
    font-family: "Jost", sans-serif;
    font-weight: 500;
    font-size: 28px;
    letter-spacing: 0.2em;
    margin-right: -0.2em;
    line-height: 1;
  }
  .person__role {
    display: block;
    margin-top: 15px;
    font-family: "Jost", sans-serif;
    font-weight: 500;
    font-size: 15px;
    letter-spacing: 0.22em;
    margin-right: -0.22em;
    line-height: 1;
  }
  .back-rule {
    position: absolute;
    left: 404px;
    top: 237px;
    width: 2px;
    height: 124px;
    background: var(--white);
  }
  .contact-list {
    position: absolute;
    left: 423px;
    top: 244px;
    margin: 0;
    padding: 0;
    list-style: none;
    font-family: "Jost", sans-serif;
    font-weight: 400;
    font-size: 21px;
    color: var(--white);
  }
  .contact-list li { height: 41px; line-height: 30px; }

  .footer-band {
    position: absolute;
    left: 0;
    bottom: 0;
    width: 1000px;
    height: 85px;
    background: var(--icy-mint);
  }
  .address {
    position: absolute;
    right: 6px;
    bottom: 20px;
    margin: 0;
    font-family: "Jost", sans-serif;
    font-weight: 400;
    font-size: 16px;
    letter-spacing: 0.1em;
    text-transform: uppercase;
    color: var(--ink);
  }
</style>
</head>
<body>
<main class="canvas">
  <section class="card-front">
    <div class="brand-ornament" role="img" aria-label="Swirling scroll ornament beside the business name"></div>
    <div class="brand-rule"></div>
    <h1 class="brand-name">
      <span class="brand-name__main">marisol's</span>
      <span class="brand-name__sub">Beauty Room</span>
    </h1>
  </section>

  <section class="card-back">
    <div class="person">
      <span class="person__first">marisol</span>
      <span class="person__last">QUENTELI</span>
      <span class="person__role">BEAUTY THERAPIST</span>
    </div>
    <div class="back-rule"></div>
    <ul class="contact-list">
      <li>Contact no.: 0412 963 174</li>
      <li>E-mail: marisolquenteli@examplemail.net</li>
      <li>Website: www.marisolsbeautyroom.example.au</li>
    </ul>

    <div class="footer-band" role="img" aria-label="Scalloped mint border pattern along the bottom edge"></div>
    <p class="address">3/218-226 Ferrow Rd, Kelsby VIC 3187</p>
  </section>
</main>
</body>
</html>
```